Veterinary Clinic Letterhead - Ridgeline Veterinary Surgery

We need a letterhead design for an established Veterinary Clinic in Mareeba called Ridgeline Veterinary Surgery. We are a moderate sized mixed animal veterinary clinic offering a wide variety of veterinary services. The design should use the same colour pattern as those in the logos supplied. The design should also include our address (58 Corvane Street, Tallowbrook, Queensland, 4871), phone number (07 4167 5830), email (admin@ridgelinevets.example.au), website (www.ridgelinevets.example.au) and our opening hours (8am to 5pm Monday to Friday and 8am to 12pm Saturday).
Target Market(s)
Pet owners
Industry/Entity Type
Veterinary
Requirements
Must have
- The logo or modification of it, business address, opening hours, website, phone number and email address

```html
<!DOCTYPE html>
<html lang="en">
<head>
<meta charset="utf-8">
<title>Ridgeline Veterinary Surgery – Letterhead</title>
<link href="https://fonts.googleapis.com/css2?family=Open+Sans:wght@400;600&family=Lato:wght@400;700&display=swap" rel="stylesheet">
<style>
  :root {
    --navy: #0d2a55;
    --navy-soft: #27487a;
    --ink: #4a4a4a;
    --ink-dark: #2f2f2f;
    --paper: #ffffff;
    --backdrop: #e4e4e4;
    --band-text: #ffffff;
  }
  html, body {
    margin: 0;
    padding: 0;
    width: 1040px;
    height: 1200px;
    overflow: hidden;
    background: var(--backdrop);
  }
  .letterhead {
    position: absolute;
    left: 53px;
    top: 0;
    width: 933px;
    height: 1200px;
    background: var(--paper);
    font-family: "Open Sans", sans-serif;
    color: var(--ink);
    overflow: hidden;
  }
  .brand {
    position: absolute;
    left: 0;
    top: 40px;
    width: 933px;
    text-align: center;
  }
  .brand-mark {
    display: block;
    width: 84px;
    height: 84px;
    margin: 0 auto 12px;
    border-radius: 50%;
    background: var(--navy);
  }
  .brand-name {
    font-weight: 600;
    font-size: 14px;
    letter-spacing: 0.5px;
    color: var(--navy);
    text-transform: uppercase;
    line-height: 1.3;
  }
  .letter-body {
    position: absolute;
    left: 89px;
    width: 753px;
    font-size: 15px;
  }
  .issue-date { top: 218px; }
  .recipient { top: 253px; line-height: 18px; }
  .salutation { top: 358px; }
  .letter-text {
    top: 408px;
    line-height: 27px;
    text-align: justify;
  }
  .letter-text p { margin: 0 0 27px; }
  .closing { top: 815px; }
  .signature {
    position: absolute;
    left: 89px;
    top: 852px;
    width: 215px;
    height: 24px;
    background: linear-gradient(90deg, rgba(60,60,60,0.18), rgba(60,60,60,0.05));
    border-radius: 3px;
  }
  .signer-name {
    position: absolute;
    left: 89px;
    top: 891px;
    font-size: 18.5px;
    color: var(--ink-dark);
  }
  .signer-title {
    position: absolute;
    left: 89px;
    top: 922px;
    font-size: 15px;
  }
  .corner-art {
    position: absolute;
    left: 753px;
    top: 939px;
    width: 180px;
    height: 261px;
    background: linear-gradient(160deg, var(--navy-soft), var(--navy));
    border-top-left-radius: 90px 120px;
    z-index: 2;
  }
  .contact-band {
    position: absolute;
    left: 0;
    top: 1101px;
    width: 933px;
    height: 99px;
    background: var(--navy);
    color: var(--band-text);
    font-family: "Lato", sans-serif;
  }
  .contact-list {
    position: absolute;
    left: 71px;
    top: 10px;
    font-size: 16px;
    line-height: 1;
  }
  .contact-row {
    display: flex;
    align-items: center;
    gap: 5px;
    height: 24px;
    white-space: nowrap;
  }
  .contact-item { display: inline-flex; align-items: center; gap: 5px; margin-right: 8px; }
  .icon { width: 17px; height: 17px; flex: none; }
  .band-divider {
    position: absolute;
    left: 481px;
    top: 0;
    width: 2px;
    height: 99px;
    background: var(--band-text);
  }
  .opening-hours {
    position: absolute;
    left: 503px;
    top: 8px;
    font-size: 17px;
    line-height: 22px;
  }
  .opening-hours h2 {
    margin: 0;
    font-size: 21px;
    font-weight: 700;
    line-height: 24px;
  }
  .opening-hours strong { font-weight: 700; }
</style>
</head>
<body>
  <main class="letterhead">
    <header class="brand">
      <span class="brand-mark"></span>
      <div class="brand-name">Ridgeline Veterinary Surgery</div>
    </header>

    <div class="letter-body issue-date">Issuing Date: May 5, 2018</div>
    <div class="letter-body recipient">
      Name Of Employee Mr. XYZABC<br>
      Address of Employee<br>
      Address Line 2 etc..
    </div>
    <div class="letter-body salutation">Dear Mr.XYZABC</div>

    <div class="letter-body letter-text">
      <p>Lorem Ipsum has been the industry's standard dummy text ever since the 1500s, when an unknown printer took a galley of type and scrambled it to make a type specimen book. It has survived not only five centuries, but also the leap into electronic typesetting, remaining essentially unchanged. It was popularised in the 1960s with the release of Lettrafix sheets containing Lorem Ipsum passages, and more recently with desktop publishing software like Quillset PageBuilder including versions of Lorem Ipsum.</p>
      <p>Lorem Ipsum is simply dummy text of the printing and typesetting industry. Lorem Ipsum has been the industry's standard dummy text ever since the 1500s, when an unknown printer took a galley of type and scrambled it to make a type specimen book.</p>
      <p>It has survived not only five centuries, but also the leap into electronic typesetting, remaining essentially unchanged. It was popularised in the 1960s with the release of Lettrafix sheets containing Lorem IpsumIpsum passages.</p>
    </div>

    <div class="letter-body closing">Yours Sincerely</div>
    <div class="signature" role="img" aria-label="Handwritten signature of Marcus Holloway"></div>
    <div class="signer-name">Marcus Holloway</div>
    <div class="signer-title">Managing Director</div>

    <div class="corner-art" role="img" aria-label="Large navy illustration of a bull's head in the bottom right corner"></div>

    <footer class="contact-band">
      <div class="contact-list">
        <div class="contact-row">
          <svg class="icon" viewBox="0 0 20 20" aria-hidden="true"><circle cx="10" cy="10" r="9.5" fill="#fff"/><path d="M10 4.5a3.5 3.5 0 0 0-3.5 3.5c0 2.6 3.5 7 3.5 7s3.5-4.4 3.5-7A3.5 3.5 0 0 0 10 4.5z" fill="#0d2a55"/><circle cx="10" cy="8" r="1.3" fill="#fff"/></svg>
          <span>58 Corvane Street, Tallowbrook, Queensland, 4871</span>
        </div>
        <div class="contact-row">
          <span class="contact-item">
            <svg class="icon" viewBox="0 0 20 20" aria-hidden="true"><circle cx="10" cy="10" r="9.5" fill="#fff"/><path d="M7 5l2 2.5-1.2 1.4a7 7 0 0 0 3.3 3.3l1.4-1.2L15 13l-1 2c-4.5 0-9-4.5-9-9z" fill="#0d2a55"/></svg>
            <span>07 4167 5830</span>
          </span>
          <span class="contact-item">
            <svg class="icon" viewBox="0 0 20 20" aria-hidden="true"><circle cx="10" cy="10" r="9.5" fill="#fff"/><rect x="5" y="6.5" width="10" height="7" rx="1" fill="#0d2a55"/><path d="M5.5 7l4.5 3.5L14.5 7" stroke="#fff" stroke-width="1" fill="none"/></svg>
            <span>admin@ridgelinevets.example.au</span>
          </span>
        </div>
        <div class="contact-row">
          <svg class="icon" viewBox="0 0 20 20" aria-hidden="true"><circle cx="10" cy="10" r="9.5" fill="#fff"/><circle cx="10" cy="10" r="5" fill="none" stroke="#0d2a55" stroke-width="1.4"/><path d="M5 10h10M10 5c-2.5 3-2.5 7 0 10M10 5c2.5 3 2.5 7 0 10" stroke="#0d2a55" stroke-width="1" fill="none"/></svg>
          <span>www.ridgelinevets.example.au</span>
        </div>
      </div>
      <div class="band-divider"></div>
      <section class="opening-hours">
        <h2>Opening Hours</h2>
        <div><strong>Monday - Friday</strong> : 8am to 5pm</div>
        <div><strong>Saturday:</strong>&nbsp; 8am to 12pm</div>
      </section>
    </footer>
  </main>
</body>
</html>
```